Corporate Travel Technology Company needs new Business Card design

We need a new business card design to reflect our re-branded company. Our company is called vendaXo (pronounced eureka) and we provide Business Intelligence and Connected Trip Oversight solutions for the corporate travel industry. Our multinational customers use our solutions to manage large travel budgets and frequent travellers, as well as to save money and reduce risk. We'd like to see designs that use the blue and green palette as well as our corporate logo (attached below). The design should communicate innovation, insight, forward thinking, contemporary, trusted.

Target Market(s)

Large multinational corporates and Travel Agencies.

Industry/Entity Type

Business

Contact Information for Business Card

Marguerite Tallis
Chief Executive
vendaXo
Phone number - +61 (0)2 8147 3092
Email address - marguerite.tallis@vendaxo.example
Mobile number - +61 (0)455 206 718
www.vendaxo.example

Font styles to use
Other font styles liked:
• Please use font as close to corporate logo as possible

Colors
0255a3
0393ce
00a990
33b8a4
33a6d7
3176b5

Requirements
Must have
• Please include the words;
• Connected Trip Oversight
• Sharpening Corporate Journey Analytics
• Use corporate logo - although icon can be stylised if needed

```html
<!DOCTYPE html>
<html lang="en">
<head>
<meta charset="utf-8">
<title>vendaXo business card</title>
<link rel="stylesheet" href="https://fonts.googleapis.com/css2?family=Open+Sans:ital,wght@0,400;0,600;1,600&display=swap">
<style>
  :root {
    --backdrop: #111213;
    --card-front: #f3f3f3;
    --card-back: #00adef;
    --brand-blue: #1ba3e0;
    --wordmark: #3f5157;
    --ink: #1e1e1e;
    --white: #ffffff;
  }
  * { margin: 0; padding: 0; box-sizing: border-box; }
  html, body {
    width: 1200px; height: 900px; overflow: hidden;
    background: var(--backdrop);
    font-family: "Open Sans", Arial, sans-serif;
  }
  .canvas { position: relative; width: 1200px; height: 900px; }
  .card {
    position: absolute; top: 184px; height: 490px; border-radius: 12px;
  }
  .card--front { left: 299px; width: 301px; background: var(--card-front); }
  .card--back { left: 645px; width: 304px; background: var(--card-back); }

  .brand { position: absolute; left: 0; right: 0; top: 42px; text-align: center; }
  .brand__mark { display: block; margin: 0 auto 6px; }
  .brand__name {
    display: block; font-size: 58px; font-weight: 400; line-height: 1;
    color: var(--wordmark); letter-spacing: 0.5px;
  }

  .person { position: absolute; left: 0; right: 0; top: 292px; text-align: center; }
  .person__name {
    font-size: 18px; font-weight: 600; color: var(--brand-blue);
    text-transform: uppercase; letter-spacing: 0.3px; line-height: 22px;
  }
  .person__role { font-size: 13px; color: var(--ink); line-height: 18px; }

  .contact { position: absolute; left: 0; right: 0; top: 357px; list-style: none; text-align: center; }
  .contact__item {
    font-size: 13px; color: var(--ink); line-height: 20.5px;
    display: flex; justify-content: center; align-items: center; gap: 3px;
  }
  .contact__icon { width: 10px; height: 10px; fill: var(--brand-blue); flex: none; }

  .tagline {
    position: absolute; left: 0; right: 0; top: 401px; text-align: center;
    color: var(--white); font-size: 15.5px; font-weight: 600; font-style: italic; line-height: 25px;
  }
</style>
</head>
<body>
<main class="canvas">
  <section class="card card--front" aria-label="Card front">
    <div class="brand">
      <svg class="brand__mark" width="44" height="44" viewBox="0 0 44 44" aria-hidden="true">
        <circle cx="22" cy="22" r="19" fill="none" stroke="var(--brand-blue)" stroke-width="4"/>
      </svg>
      <span class="brand__name">vendaXo</span>
    </div>

    <div class="person">
      <p class="person__name">Marguerite Tallis</p>
      <p class="person__role">Chief Executive</p>
    </div>

    <ul class="contact">
      <li class="contact__item">
        <svg class="contact__icon" viewBox="0 0 10 10" aria-hidden="true"><path d="M2 0.5l2 2-1 1.2c.6 1.3 1.6 2.3 2.9 2.9L7 5.5l2 2-1.2 1.8C4.2 9 1 5.8.7 1.7z"/></svg>
        +61 (0)2 8147 3092
      </li>
      <li class="contact__item">
        <svg class="contact__icon" viewBox="0 0 10 10" aria-hidden="true"><rect x="2" y="0" width="6" height="10" rx="1"/><rect x="3" y="1.2" width="4" height="6.5" fill="var(--card-front)"/></svg>
        +61 (0)455 206 718
      </li>
      <li class="contact__item">
        <svg class="contact__icon" viewBox="0 0 10 10" aria-hidden="true"><rect x="0" y="2" width="10" height="7"/><path d="M0.5 2.5L5 6l4.5-3.5" fill="none" stroke="var(--card-front)" stroke-width="1"/></svg>
        marguerite.tallis@vendaxo.example
      </li>
      <li class="contact__item">
        <svg class="contact__icon" viewBox="0 0 10 10" aria-hidden="true"><path d="M4 6L6 4M3.2 5.2L1.6 6.8a1.5 1.5 0 0 0 2.1 2.1L5.3 7.3M6.8 4.8l1.6-1.6a1.5 1.5 0 0 0-2.1-2.1L4.7 2.7" fill="none" stroke="var(--brand-blue)" stroke-width="1.3" stroke-linecap="round"/></svg>
        www.vendaxo.example
      </li>
    </ul>
  </section>

  <section class="card card--back" aria-label="Card back">
    <p class="tagline">Connected Trip Oversight<br>Sharpening Corporate Journey Analytics</p>
  </section>
</main>
</body>
</html>
```